Business Card Design Project

I have a two letter domain name qo.com.au (lower case font please). I want a business card, cum logo that is die cut (around the qo segment at least) that fits standard business card size.
qo is all about what 'I am' - a journalist, blogger, analyst, commentator. My mantra is "I wander so qo'.
The reverse of the card only needs my name Lon Fitch, email lon@qo.com.au and mobile +61 400 555 817
Target Market(s)
Mainly people that will use my professional writing services and suppliers that will provide product for review
Industry/Entity Type
Business
Requirements
Must have
- One side is qo.com.au (hint - the .com.au can be vertical or horizontal to fit - the qo should be as large as possible).
The other requires large size font name, email and phone details (so no one needs glasses to read it).
The die cut can be just to highlight the qo segment - need not be around the whole card.
Font used in the past was Belwe (old style - very much like the i used in the information symbol).
Colours - no preference - prefer two colour to process colour but can also be an outline font instead of solid colour.

```html
<!DOCTYPE html>
<html lang="en">
<head>
<meta charset="utf-8">
<title>qo.com.au business card</title>
<link rel="stylesheet" href="https://fonts.googleapis.com/css2?family=Arimo&family=Gentium+Book+Plus&family=Tinos:ital,wght@1,700&family=Tinos:wght@700&display=swap">
<style>
  :root {
    --paper: #ffffff;
    --ink: #111111;
    --brand-red: #ee0000;
    --role-cyan: #33f2f2;
    --frame-yellow: #ffff00;
    --frame-edge: #000000;
  }
  html, body {
    margin: 0;
    padding: 0;
    width: 1200px;
    height: 655px;
    overflow: hidden;
    background: var(--paper);
  }
  .card {
    position: relative;
    width: 1200px;
    height: 655px;
    background: var(--paper);
    overflow: hidden;
  }
  .frame {
    position: absolute;
    inset: 0;
  }
  .frame .bar {
    fill: var(--frame-yellow);
    stroke: var(--frame-edge);
    stroke-width: 2;
  }
  .brand {
    position: absolute;
    margin: 0;
    color: var(--brand-red);
    font-family: "Arimo", Arial, sans-serif;
    font-weight: 400;
    line-height: 1;
    white-space: nowrap;
  }
  .brand--corner { font-size: 30px; }
  .brand--corner-top { left: 4px; top: 14px; }
  .brand--corner-bottom { left: 1040px; top: 584px; }
  .brand--hero { left: 84px; top: 150px; font-size: 56px; }
  .brand--hero .brand__name {
    font-size: 210px;
    letter-spacing: -6px;
  }
  .mantra {
    position: absolute;
    left: 452px;
    top: 78px;
    margin: 0;
    color: var(--ink);
    font-family: "Tinos", "Times New Roman", serif;
    font-style: italic;
    font-weight: 700;
    font-size: 50px;
    line-height: 1;
    white-space: nowrap;
  }
  .mantra__word {
    font-style: normal;
    font-size: 80px;
    margin-left: 14px;
  }
  .contact {
    position: absolute;
    left: 97px;
    top: 385px;
    margin: 0;
    font-family: "Gentium Book Plus", Georgia, serif;
    font-size: 38px;
    line-height: 54px;
    color: var(--ink);
    font-style: normal;
  }
  .contact__line { display: block; }
  .contact__line--indent { padding-left: 98px; }
  .roles {
    position: absolute;
    left: 570px;
    top: 278px;
    margin: 0;
    padding: 0;
    list-style: none;
    color: var(--role-cyan);
    font-family: "Arimo", Arial, sans-serif;
    font-size: 54px;
    line-height: 65px;
  }
  .roles__item { padding-left: 164px; }
  .roles__item--lead { padding-left: 0; }
</style>
</head>
<body>
<main class="card">
  <svg class="frame" width="1200" height="655" viewBox="0 0 1200 655" aria-hidden="true">
    <rect class="bar" x="129" y="2" width="1060" height="10"/>
    <rect class="bar" x="1178" y="2" width="10" height="570"/>
    <rect class="bar" x="478" y="22" width="690" height="9"/>
    <rect class="bar" x="1158" y="22" width="9" height="373"/>
    <rect class="bar" x="2" y="83" width="10" height="566"/>
    <rect class="bar" x="2" y="639" width="1060" height="10"/>
    <rect class="bar" x="25" y="254" width="9" height="370"/>
    <rect class="bar" x="25" y="615" width="690" height="9"/>
  </svg>

  <p class="brand brand--corner brand--corner-top">qo.com.au</p>

  <p class="mantra">I wander so<span class="mantra__word">qo'</span></p>

  <p class="brand brand--hero"><span class="brand__name">qo</span>.com.au</p>

  <address class="contact">
    <span class="contact__line">mr. Lon Fitch</span>
    <span class="contact__line contact__line--indent">lon@qo.com.au</span>
    <span class="contact__line contact__line--indent">+61400555817</span>
  </address>

  <ul class="roles">
    <li class="roles__item roles__item--lead">I am - journalist</li>
    <li class="roles__item">blogger</li>
    <li class="roles__item">analyst</li>
    <li class="roles__item">commentator</li>
  </ul>

  <p class="brand brand--corner brand--corner-bottom">qo.com.au</p>
</main>
</body>
</html>
```